Publisher needs a book cover design for ‘Lanterns Over the Marsh Gate’ book

We need a book cover (front, back, spine) for the 2nd edition of a book entitled ‘Lanterns Over the Marsh Gate’ and subtitled ‘the quiet geography of tidal winds, ferry routes and harbour lanterns’ (inverted commas not to be part of the title and subtitle). The author is Rupert Calloway. The publisher is Vellmark Press. The finished size of the paperback version will be the industry standard 9" x 6". There will be paperback, hardback, and e-book versions. The final number of pages is expected to be in the region 150-180 pages. Text for the back cover is not yet available, but at the bottom of the back cover should be publisher logo (rectangular) on the left and space for the ISBN bar code on the right. The circular logo should be on the spine. The design should be original and not include any stock images that have been created by someone else or may require obtaining a copyright licence to use. Symbols in common use and not copyrighted are probably ok. There are no required images, photographs or symbols except the publisher logo at the left bottom of the back cover and lower spine. Spine lettering should be UK/US style with the top of the writing nearest the front cover. The designer is free to be creative using appropriate diagrams, symbols or abstract designs. Rectangular and circular variants of the publisher logo are attached. Designers are assured that when evaluating designs absolutely no notice whatsoever is taken of a designer's Pixo Rally ranking or status; We are completely output driven, so what matters is the design, not the ranking or status of the designer. In a similar way, designs are not evaluated as 'good' or 'bad' - the winning design will be chosen after review by a design review panel and is not decided arbitrarily by a single person. All submitted designs should be capable of effective copyright assignment.

Target Market(s)

Practitioners, parents, teachers, pupils and academics concerned with child protection, safeguarding and the elimination of emotional abuse of children in the classroom

Font styles to use
Serif
Sans Serif

Requirements
Must have
• • Title, author, edition, subtitle, publisher logo
Nice to have
• • Originality, innovation
Should not have
• • Stock images or anything else requiring additional copyright discussions and negotiations.

```html
<!DOCTYPE html>
<html lang="en">
<head>
<meta charset="utf-8">
<title>Lanterns Over the Marsh Gate — Cover</title>
<link rel="stylesheet" href="https://fonts.googleapis.com/css2?family=EB+Garamond:wght@400;500&family=Courier+Prime:wght@700&display=swap">
<style>
  :root {
    --bg: #e7e6f0;
    --paper: #ffffff;
    --paper-shade: #ececec;
    --ink: #2b2b2b;
    --red: #e8313a;
    --art-warm: #f3c23a;
    --art-soft: #f7dd8e;
  }
  * { margin: 0; padding: 0; box-sizing: border-box; }
  html, body { width: 1200px; height: 963px; overflow: hidden; background: var(--bg); }
  .canvas { position: relative; width: 1200px; height: 963px; }

  .front-cover {
    position: absolute; left: 236px; top: 77px; width: 495px; height: 744px;
    background: linear-gradient(160deg, var(--paper-shade) 0%, var(--paper) 40%, var(--paper) 100%);
    box-shadow: 0 6px 18px rgba(60, 55, 110, 0.18);
    font-family: "EB Garamond", Georgia, serif;
    color: var(--ink);
    text-align: center;
  }
  .title-top {
    position: absolute; top: 82px; left: 0; width: 100%;
    font-size: 32px; letter-spacing: 0.5px; line-height: 1;
  }
  .title-main {
    position: absolute; top: 122px; left: 0; width: 100%;
    font-family: "Courier Prime", "Courier New", monospace; font-weight: 700;
    font-size: 112px; line-height: 1; color: var(--red); letter-spacing: 2px;
  }
  .title-bottom {
    position: absolute; top: 230px; left: 0; width: 100%;
    font-size: 23px; letter-spacing: 3px; line-height: 1;
  }
  .subtitle {
    position: absolute; top: 308px; left: 88px; width: 320px;
    font-size: 18px; line-height: 1.05;
  }
  .cover-art {
    position: absolute; left: 70px; top: 430px; width: 355px; height: 150px;
    background: radial-gradient(ellipse at 50% 55%, var(--art-warm) 0%, var(--art-soft) 30%, rgba(255,255,255,0) 70%);
  }
  .edition {
    position: absolute; top: 615px; left: 0; width: 100%;
    font-size: 20px; line-height: 1.2;
  }
  .author {
    position: absolute; top: 694px; left: 0; width: 100%;
    font-size: 20px; line-height: 1.2;
  }

  .spine {
    position: absolute; left: 880px; top: 77px; width: 86px; height: 750px;
    background: var(--paper);
    box-shadow: 0 6px 18px rgba(60, 55, 110, 0.18);
    font-family: "EB Garamond", Georgia, serif;
    color: var(--ink);
  }
  .spine-edition {
    position: absolute; top: 22px; left: 0; width: 100%; height: 20px;
    background: var(--red); color: #fff;
    font-size: 14px; line-height: 20px; text-align: center;
  }
  .spine-title {
    position: absolute; top: 64px; left: 50%; transform: translateX(-50%);
    writing-mode: vertical-rl;
    white-space: nowrap;
    display: flex; align-items: center;
  }
  .spine-title-small { font-size: 18px; letter-spacing: 1.5px; }
  .spine-title-main {
    font-family: "Courier Prime", "Courier New", monospace; font-weight: 700;
    font-size: 46px; color: var(--red); line-height: 1; margin: 6px 0;
  }
  .spine-author {
    position: absolute; top: 572px; left: 50%; transform: translateX(-50%);
    writing-mode: vertical-rl; white-space: nowrap;
    font-size: 16px; color: var(--red);
  }
  .spine-publisher {
    position: absolute; bottom: 10px; left: 0; width: 100%;
    display: flex; flex-direction: column; align-items: center; gap: 3px;
  }
  .publisher-dot { width: 26px; height: 26px; border-radius: 50%; background: var(--ink); }
  .publisher-name { font-size: 9px; color: var(--ink); text-align: center; line-height: 1; }
</style>
</head>
<body>
<main class="canvas">
  <section class="front-cover">
    <div class="title-top">LANTERNS OVER THE</div>
    <h1 class="title-main">MARSH</h1>
    <div class="title-bottom">GATE</div>
    <p class="subtitle">The quiet geography of tidal winds, ferry routes and harbour lanterns</p>
    <div class="cover-art" role="img" aria-label="Photograph of a yellow pencil snapped in two on a white surface"></div>
    <p class="edition">2nd Edition</p>
    <p class="author">Rupert Calloway</p>
  </section>

  <aside class="spine">
    <div class="spine-edition">2nd Edition</div>
    <div class="spine-title">
      <span class="spine-title-small">LANTERNS OVER THE</span>
      <span class="spine-title-main">MARSH</span>
      <span class="spine-title-small">GATE</span>
    </div>
    <div class="spine-author">Rupert Calloway</div>
    <div class="spine-publisher">
      <span class="publisher-dot"></span>
      <span class="publisher-name">Vellmark Press</span>
    </div>
  </aside>
</main>
</body>
</html>
```